Visitenkarten für regionale Fluggesellschaft
Zielgruppe
Wir sind eine regionale Fluggesellschaft, die seit zehn Jahren Flüge von Mannheim aus anbietet.
Aufgabenstellung
Gern möchten wir das Design der bisherigen Visitenkarten überarbeiten lassen. Die bisherigen sind seit über fünf Jahren im Einsatz. Es darf moderner aussehen. Vielleicht auch mit Symbolen (wie Font Awesome) gearbeitet werden.
Die Adresse sollte sein:
LHV Lindenhof-Vogtmar Jet GmbH
Birkenweiler Talstr. 48
74391 Mannheim

```html
<!DOCTYPE html>
<html lang="de">
<head>
<meta charset="utf-8">
<title>Visitenkarten – Lindenhof-Vogtmar Jet</title>
<link href="https://fonts.googleapis.com/css2?family=Open+Sans:wght@400;600;700&display=swap" rel="stylesheet">
<style>
  :root {
    --stage: #2a2b2d;
    --brand-blue: #0093d6;
    --sky-light: #8fcbee;
    --leaf-green: #b9d24a;
    --paper: #ffffff;
    --ink: #2b2b2b;
  }
  * { margin: 0; padding: 0; box-sizing: border-box; }
  html, body { width: 1200px; height: 978px; overflow: hidden; }
  body {
    background: var(--stage);
    font-family: "Open Sans", Arial, sans-serif;
    position: relative;
  }
  .card {
    position: absolute;
    width: 540px;
    height: 350px;
    top: 314px;
    overflow: hidden;
  }
  /* Front */
  .card-front { left: 40px; background: var(--brand-blue); color: var(--paper); }
  .front-wordmark {
    position: absolute; left: 0; right: 0; top: 140px;
    display: flex; align-items: center; justify-content: center; gap: 16px;
    font-size: 34px; font-weight: 600; letter-spacing: 0.5px;
  }
  .front-wordmark .mark-dot {
    width: 22px; height: 22px; border-radius: 50%; background: var(--paper);
  }
  .front-url {
    position: absolute; left: 0; right: 0; bottom: 42px;
    text-align: center; font-size: 16px; font-weight: 400;
  }
  /* Back */
  .card-back { left: 620px; background: var(--paper); color: var(--ink); }
  .back-wordmark {
    position: absolute; left: 30px; top: 48px;
    display: flex; align-items: center; gap: 12px;
    font-size: 54px; font-weight: 700; color: var(--sky-light); letter-spacing: 2px;
  }
  .back-wordmark .mark-square { width: 26px; height: 26px; background: var(--sky-light); }
  .person { position: absolute; left: 290px; top: 42px; width: 230px; }
  .person-name { font-size: 22px; font-weight: 700; color: var(--brand-blue); letter-spacing: 0.3px; }
  .person-role { font-size: 14px; margin-top: 2px; }
  .person-rule { height: 1.5px; background: var(--brand-blue); margin-top: 14px; }
  .contact-list { list-style: none; margin-top: 16px; font-size: 13px; line-height: 22px; }
  .contact-list li { display: flex; align-items: center; gap: 10px; }
  .contact-list svg { width: 14px; height: 14px; flex: none; fill: var(--brand-blue); }
  .address {
    position: absolute; left: 36px; bottom: 66px;
    display: flex; gap: 12px; font-size: 14px; line-height: 20px;
  }
  .address svg { width: 14px; height: 18px; margin-top: 2px; fill: var(--brand-blue); flex: none; }
  .band { position: absolute; left: 0; bottom: 0; width: 540px; height: 40px; }
</style>
</head>
<body>

  <section class="card card-front" aria-label="Vorderseite">
    <div class="front-wordmark"><span class="mark-dot"></span>Lindenhof-Vogtmar Jet</div>
    <div class="front-url">flyLHV-beispiel.de</div>
  </section>

  <section class="card card-back" aria-label="Rückseite">
    <div class="back-wordmark"><span class="mark-square"></span>LHV</div>

    <div class="person">
      <div class="person-name">TOBIAS QUINDT</div>
      <div class="person-role">Geschäftsführer</div>
      <div class="person-rule"></div>
      <ul class="contact-list">
        <li><svg viewBox="0 0 24 24"><path d="M6.6 10.8a15.1 15.1 0 0 0 6.6 6.6l2.2-2.2c.3-.3.7-.4 1-.2 1.1.4 2.3.6 3.6.6.6 0 1 .4 1 1V20c0 .6-.4 1-1 1A17 17 0 0 1 3 4c0-.6.4-1 1-1h3.5c.6 0 1 .4 1 1 0 1.3.2 2.5.6 3.6.1.3 0 .7-.2 1z"/></svg>+49 621 555 019 42</li>
        <li><svg viewBox="0 0 24 24"><path d="M7 1h10a2 2 0 0 1 2 2v18a2 2 0 0 1-2 2H7a2 2 0 0 1-2-2V3a2 2 0 0 1 2-2zm0 3v14h10V4zm5 15.5a1.2 1.2 0 1 0 0 2.4 1.2 1.2 0 0 0 0-2.4z"/></svg>+49 151 555 038 71</li>
        <li><svg viewBox="0 0 24 24"><path d="M2 5h20v14H2zm2 2v.5l8 5 8-5V7zm0 2.8V17h16V9.8l-8 5z"/></svg>tobias.quindt@flylhv-beispiel.de</li>
      </ul>
    </div>

    <div class="address">
      <svg viewBox="0 0 24 32"><path d="M12 0A11 11 0 0 0 1 11c0 8 11 21 11 21s11-13 11-21A11 11 0 0 0 12 0zm0 15a4 4 0 1 1 0-8 4 4 0 0 1 0 8z"/></svg>
      <div>LHV Lindenhof-Vogtmar Jet GmbH<br>Birkenweiler Talstr. 48<br>74391 Mannheim</div>
    </div>

    <svg class="band" viewBox="0 0 540 40" preserveAspectRatio="none" aria-hidden="true">
      <polygon points="0,28 360,28 380,40 0,40" fill="var(--leaf-green)"/>
      <polygon points="350,28 540,0 540,40 372,40" fill="var(--brand-blue)"/>
    </svg>
  </section>

</body>
</html>
```